Brand refresh of quote, work docket and Fire certificate documents

I would like a refresh of our document suit including

1. Front page called VANTO3 Proposal
2. Quote document template
3. Work docket template
4. Fire certificate template - to look like a professional complaint certificate

Examples of documents are attached.

```html
<!DOCTYPE html>
<html lang="en">
<head>
<meta charset="utf-8">
<title>VANTO3 Document Suite</title>
<link href="https://fonts.googleapis.com/css2?family=Open+Sans:ital,wght@0,400;0,600;0,700;0,800;1,400;1,700&family=Russo+One&display=swap" rel="stylesheet">
<style>
:root{
  --red:#c8161d;
  --orange:#f07f22;
  --ink:#222;
  --tag:#d0343a;
  --black:#0a0a0a;
  --paper:#ffffff;
  --cream:#faf6ee;
  --muted:#f3f3f3;
}
*{margin:0;padding:0;box-sizing:border-box}
html,body{width:1200px;height:3123px;overflow:hidden;background:#fff}
body{position:relative;font-family:"Open Sans",Arial,sans-serif;color:var(--ink)}
.section-title{position:absolute;left:0;width:1200px;text-align:center;font-weight:700;font-size:35px;letter-spacing:.5px}
.section-title span{border-bottom:2px solid var(--ink);padding-bottom:2px}
.page{position:absolute;width:413px;height:584px;background:var(--paper);box-shadow:0 8px 22px rgba(0,0,0,.2);overflow:hidden;font-size:7.5px;line-height:1.35}

.cover{left:394px;top:189px;background:var(--black)}
.cover-brand{position:absolute;top:46px;left:0;width:100%;text-align:center;color:#fff}
.brand-word{font-weight:800;font-size:50px;line-height:1;letter-spacing:1px}
.brand-tag{font-size:7px;letter-spacing:3.5px;margin-top:4px}
.cover-pill{position:absolute;left:117px;top:118px;width:177px;height:23px;border-radius:12px;background:var(--red);color:#fff;text-align:center;font-size:12px;line-height:23px;letter-spacing:2.5px;font-weight:600}
.cover-frame{position:absolute;left:0;top:162px;width:354px;height:357px;background:#fff;border-radius:0 70px 70px 0}
.cover-photo{position:absolute;left:0;top:12px;width:340px;height:333px;border-radius:0 60px 60px 0;background:linear-gradient(180deg,#d9271f 0%,#e9522a 45%,#f59022 100%)}
.cover-url{position:absolute;bottom:26px;width:100%;text-align:center;color:var(--orange);font-size:11px;font-weight:600;letter-spacing:.5px}

.doc-head{height:64px;background:var(--black);color:#fff;position:relative}
.doc-head .logo{position:absolute;left:18px;top:14px}
.doc-head .logo .brand-word{font-size:28px}
.doc-head .logo .brand-tag{font-size:4.5px;letter-spacing:2px;margin-top:2px}
.doc-head .addr{position:absolute;right:16px;top:9px;text-align:right;font-size:7.5px;line-height:1.25}
.doc-head .addr b{font-weight:700}
.body{padding:0 28px}
.bar{height:18px;border-radius:2px 9px 9px 2px;background:linear-gradient(90deg,var(--red),var(--orange));color:#fff;font-weight:700;font-size:7.5px;line-height:18px;padding-left:8px;margin-top:8px}
.item{padding-left:9px;margin-top:5px}
.item + .item{margin-top:3px}
.tag{color:var(--tag);font-style:italic;padding-left:9px;margin-top:3px}
.q{color:var(--tag);font-style:italic;margin-left:12px}
.red-head{color:var(--red);font-weight:700;font-size:9.5px}
.total{display:flex;justify-content:center;margin-top:14px}
.total .lbl{background:var(--red);color:#fff;font-weight:700;font-size:8.5px;padding:0 9px;height:18px;line-height:18px;border-radius:9px 0 0 9px}
.total .amt{background:var(--black);color:#fff;font-weight:800;font-size:9.5px;padding:0 10px;height:18px;line-height:18px;border-radius:0 9px 9px 0}

.docket-a{left:178px;top:915px}
.docket-b{left:608px;top:915px}
.quote-a{left:178px;top:1642px}
.quote-b{left:608px;top:1642px}

.labour-row{display:flex;margin-top:4px}
.materials{display:flex;gap:12px;margin-top:4px}
.mat-list{width:170px}
.mat-list div{display:flex;justify-content:space-between;margin-top:3px}
.mat-list b{font-weight:700}
.breakdown{flex:1;background:var(--muted);border:1px solid #ddd;border-radius:8px;padding:8px 10px;margin-top:-4px}
.breakdown div{margin-top:4px}

.quote-word{font-family:"Russo One",Arial,sans-serif;color:var(--red);font-size:27px;letter-spacing:1px;margin-top:8px}
.abn{position:absolute;right:16px;top:68px;font-weight:700;font-size:7.5px}

.cert{left:394px;top:2369px;background:linear-gradient(180deg,#d11f1c 0%,#ec6524 55%,#f5901f 100%);padding:16px}
.cert-inner{width:100%;height:100%;background:var(--cream);text-align:center;position:relative;padding-top:20px}
.cert .brand-word{font-size:46px;color:#2a2a2a}
.cert .brand-tag{color:#555;font-size:6.5px}
.cert-title{font-family:"Russo One",Arial,sans-serif;color:var(--red);font-size:22px;line-height:1.15;margin-top:18px;letter-spacing:.5px}
.label{color:var(--red);font-weight:700;font-size:7px;letter-spacing:.5px}
.big{font-weight:700;font-size:15px;line-height:1.2}
.cert-pill{display:inline-block;background:var(--orange);color:#222;font-weight:700;font-size:8px;padding:3px 10px;border-radius:10px;margin-top:12px}
.cert p{font-size:7.5px;line-height:1.3;padding:0 34px;margin-top:10px}
.signed{display:flex;justify-content:center;align-items:center;gap:12px;margin-top:16px;font-size:7.5px}
.sig{display:inline-block;width:42px;height:14px;background:#d8d4cc;border-radius:3px;vertical-align:middle}
</style>
</head>
<body>

<div class="section-title" style="top:108px"><span>Cover Page</span></div>
<div class="page cover">
  <div class="cover-brand"><div class="brand-word">VANTO3</div><div class="brand-tag">PASSIVE FIRE PROTECTION</div></div>
  <div class="cover-pill">VANTO3 PROPOSAL</div>
  <div class="cover-frame"><div class="cover-photo" role="img" aria-label="Photo of a site worker in a hard hat and hi-vis vest, seen from above, holding a tablet"></div></div>
  <div class="cover-url">WWW.VANTO3.COM.AU</div>
</div>

<div class="section-title" style="top:840px"><span>Work Docket</span></div>
<div class="page docket-a">
  <div class="doc-head">
    <div class="logo"><div class="brand-word">VANTO3</div><div class="brand-tag">PASSIVE FIRE PROTECTION</div></div>
    <div class="addr"><b>VANTO3 Pty Ltd</b><br><b>3/22</b> Ridgeline Street<br>Eastfield VIC 3095<br>ABN: 98 765 432 101<br>admin@vanto3.com.au</div>
  </div>
  <div class="body">
    <div style="margin-top:18px">26th October, 2023</div>
    <div style="margin-top:8px"><b>Rossetti Builders</b><br>48 Harbour St<br>Dockside VIC 3011<br><b>Marco</b></div>
    <div class="red-head" style="margin-top:14px">Work Docket: 1188</div>
    <div style="margin-top:4px">Works completed at <b>14 Linden Street, Ashgrove Park</b> as directed by <b>Marco</b> of<br><b>Rossetti Builders</b> as listed below.</div>
    <div style="margin-top:6px;font-weight:700">Works Completed:</div>
    <div class="bar">Basement 1 – Fan Room</div>
    <div class="item">1 x 20mm x 20mm penetration with conduit through blockwork wall <span class="q">(?)</span></div>
    <div class="bar" style="margin-top:14px">Basement 1 – Apartment 38 Garage</div>
    <div class="item">2 x 100mm x 100mm penetration with sprinkler pipe &amp; wrap through slab wall.</div>
    <div class="tag">(Wet Fire)</div>
    <div class="bar">Basement 1 – Apartment 34 Garage</div>
    <div class="item">2 x 100mm x 100mm penetration with sprinkler pipe &amp; wrap through slab wall.</div>
    <div class="tag">(Wet Fire)</div>
    <div class="bar">Basement 1 – Apartment 30 Garage</div>
    <div class="item">2 x 100mm x 100mm penetration with sprinkler pipe &amp; wrap through slab wall.</div>
    <div class="tag">(Wet Fire)</div>
    <div class="bar">Basement 1 – Apartment 28</div>
    <div class="item">5mtrs of caulking through slab wall (one side only)</div>
    <div class="tag">(Brickies)</div>
    <div class="bar">Basement 1 – Apartment 28</div>
    <div class="item">5mtrs of caulking through slab wall (one side only)</div>
    <div class="tag">(Brickies)</div>
  </div>
</div>

<div class="page docket-b">
  <div class="body" style="padding-top:22px">
    <div class="bar">Basement 1 – Back Stairwell</div>
    <div class="item">1 x 400mm x 400mm penetration empty through blockwork wall</div>
    <div class="tag">(Builder)</div>
    <div class="bar">Basement 1 – Apartment Bin Room</div>
    <div class="item">1 x 80mm x 80mm penetration with sprinkler pipe &amp; wrap through blockwork wall</div>
    <div class="tag">(Wet Fire)</div>
    <div class="item">2 x 20mm x 20mm penetration with conduit through blockwork wall <span class="q">(?)</span></div>
    <div class="item">2 x 20mm x 20mm penetration with conduit through blockwork wall <span class="q">(?)</span></div>
    <div class="bar">Basement 1 – Comms Room</div>
    <div class="item">2 x 300mm x 300mm penetration empty through slab wall</div>
    <div class="tag">(Builder)</div>
    <div class="bar">Basement 1 – Switchboard Room</div>
    <div class="item">1 x 400mm x 100mm penetration empty through blockwork wall</div>
    <div class="tag">(Builder)</div>
    <div class="item">12mtrs of caulking through blockwork wall (one side only)</div>
    <div class="tag">(Brickies)</div>
    <div style="border-top:1px solid #ddd;margin:12px 0 10px"></div>
    <div class="red-head" style="padding-left:9px">Labour</div>
    <div class="labour-row" style="padding-left:9px"><span style="width:54px">21/10/23</span><span style="width:95px">2 Men x 5hrs = 10hrs</span><b>$1500</b></div>
    <div style="padding-left:63px;font-style:italic;margin-top:3px">(time &amp; a half rate)</div>
    <div class="red-head" style="padding-left:9px;margin-top:8px">Materials</div>
    <div class="materials" style="padding-left:9px">
      <div class="mat-list">
        <div><span>1 x Fire Mortar (20kg bag)</span><b>$150</b></div>
        <div><span>2 x Rod (Bundle</span><b>$100</b></div>
        <div><span>15 x Caulk (Ltr)</span><b>$375</b></div>
        <div><span>4 x Fire Sealant 300ml</span><b>$120</b></div>
        <div><span>1 x Pipe Wrap 40 (Roll)</span><b>$220</b></div>
        <div><span>¾ x Cable Wrap (Roll)</span><b>$450</b></div>
      </div>
      <div class="breakdown">
        <div class="red-head" style="margin-top:0">Breakdown</div>
        <div>Conduits (unknown) 10% - 291.50 + GST</div>
        <div>Wet Fire 45% - $1,311 + GST</div>
        <div>Brickies 20% - $583 + GST</div>
        <div>Builder 25% - $728.75 + GST</div>
      </div>
    </div>
    <div class="total"><span class="lbl">Total Price for Labour &amp; Materials</span><span class="amt">$2,915 + GST</span></div>
  </div>
</div>

<div class="section-title" style="top:1567px"><span>Quote</span></div>
<div class="page quote-a">
  <div class="doc-head">
    <div class="logo"><div class="brand-word">VANTO3</div><div class="brand-tag">PASSIVE FIRE PROTECTION</div></div>
    <div class="addr"><b>VANTO3 Pty Ltd</b><br><b>3/22</b> Ridgeline Street<br>Eastfield VIC 3095<br>ABN: 98 765 432 101<br>admin@vanto3.com.au</div>
  </div>
  <div class="abn">ABN: 98 765 432 101</div>
  <div class="body" style="padding-left:19px;padding-right:28px">
    <div class="quote-word">QUOTE</div>
    <div style="margin-top:6px">11<sup>th</sup> July, 2025</div>
    <div style="margin-top:10px;font-weight:700;font-size:9px">QUOTE NUMBER: 2252</div>
    <div style="margin-top:12px;color:var(--red);font-weight:700">Northgate Concepts Pty Ltd</div>
    <div style="font-weight:700">Sam Whitfield</div>
    <div style="margin-top:4px">Thank you for allowing us to provide a quotation for your fire rating requirements. Works to be completed as per inspection at <b>512 Kestrel Road, Elmwood</b> as listed below.</div>
    <div class="bar" style="margin-top:18px">Level 5 – Electrical Cupboard</div>
    <div class="item" style="margin-top:6px">1 x 700mm x 150mm penetration with cables &amp; wrap through slab floor</div>
    <div class="bar" style="margin-top:11px">Level 4 – Electrical Cupboard</div>
    <div class="item" style="margin-top:6px">1 x 700mm x 150mm penetration with cables &amp; wrap through slab floor</div>
    <div class="bar" style="margin-top:11px">Level 3 – Electrical Cupboard</div>
    <div class="item" style="margin-top:6px">1 x 700mm x 150mm penetration with cables &amp; wrap through slab floor</div>
    <div class="bar" style="margin-top:11px">Level 2 – Electrical Cupboard</div>
    <div class="item" style="margin-top:6px">1 x 700mm x 150mm penetration with cables &amp; wrap through slab floor</div>
    <div class="bar" style="margin-top:11px">Level 1 – Electrical Cupboard</div>
    <div class="item" style="margin-top:6px">1 x 700mm x 150mm penetration with cables &amp; wrap through slab floor</div>
    <div class="bar" style="margin-top:11px">Level 1 – Comms Cupboard</div>
    <div class="item" style="margin-top:6px">1 x 500mm x 150mm penetration with cables &amp; wrap through slab floor</div>
    <div class="bar" style="margin-top:11px">Ground Floor – Electrical Cupboard</div>
    <div class="item" style="margin-top:6px">1 x 700mm x 150mm penetration empty through slab floor</div>
    <div class="bar" style="margin-top:11px">Ground Floor – Comms Cupboard</div>
    <div class="item" style="margin-top:6px">1 x 500mm x 150mm penetration empty through slab floor</div>
  </div>
</div>

<div class="page quote-b">
  <div class="body" style="padding-top:17px;padding-left:27px">
    <div class="bar">Ground Floor – Switchroom</div>
    <div class="item" style="padding-right:60px">2 x 600mm x 100mm penetration with cable tray &amp; wrap (ceiling to be cut) through speed panel wall.</div>
    <div class="item" style="padding-right:60px">1 x 200mm x 100mm penetration with cable tray &amp; wrap (ceiling to be cut) through speed panel wall</div>
    <div class="item">1 x 700mm x 150mm penetration with cables &amp; wrap through slab floor</div>
    <div class="item">1 x 500mm x 150mm penetration with cables &amp; wrap through slab floor</div>
    <div class="bar">Basement 1 – Carpark</div>
    <div class="item" style="padding-right:40px">1 x 700mm x 150mm penetration with cables &amp; wrap through slab floor (smoke seal only).</div>
    <div class="item" style="padding-right:40px">1 x 500mm x 150mm penetration with cables through slab floor (smoke seal only).</div>
    <div style="color:var(--tag);font-style:italic;font-weight:700;margin-top:10px;padding-left:9px">*15 penetrations in total</div>
    <div style="color:var(--orange);font-style:italic;font-weight:700;padding-left:9px;padding-right:20px">*Includes penetration ID labels, fire certificate &amp; compliance fire penetration report</div>
    <div class="total" style="margin-top:14px"><span class="lbl">Total Price for Labour &amp; Materials</span><span class="amt">$3,750 + GST</span></div>
    <div style="margin-top:14px;padding-left:9px">Quoted price for installation and certification of the approved proprietary fire resistance tested products &amp; systems to AS1530 part 4 to maintain the required <b>FRL -/120/120</b> of the building element.</div>
    <div style="display:flex;margin-top:10px;font-size:6.5px"><span style="color:var(--tag);font-weight:700;width:54px">*Please note:</span><span>Normal working hours 7am –3:30pm Monday to Friday<br>Penalty rates apply for works after hours<br>Clear access required at all times with priority.<br>Contractor car parking to be provided</span></div>
    <div style="text-align:center;color:var(--red);font-weight:700;font-size:8.5px;margin-top:14px">VALID 90 DAYS &nbsp;|&nbsp; TERMS: 30 DAYS &nbsp;|&nbsp; NO RETENTION</div>
    <div style="text-align:center;font-weight:700;font-size:8.5px;margin-top:4px">Purchase Order required before job start</div>
    <div style="text-align:center;font-weight:700;font-size:8.5px;margin-top:2px">Fire Certification Certificate will only be provided upon full payment</div>
    <div style="margin-top:12px;padding-left:9px">To accept this quotation, please sign here and return</div>
    <div style="margin-top:18px;padding-left:9px">Sign: ............................................................ &nbsp;&nbsp;Date: ..............................................................</div>
    <div style="margin-top:7px;padding-left:9px">We look forward to proceeding upon your direction.</div>
    <div style="margin-top:14px;padding-left:9px">Kind Regards,</div>
    <div style="padding-left:9px;margin-top:2px"><span class="sig" role="img" aria-label="Handwritten signature"></span></div>
    <div style="padding-left:9px;font-weight:700">Liam Carver</div>
  </div>
</div>

<div class="section-title" style="top:2294px"><span>Certificate</span></div>
<div class="page cert">
  <div class="cert-inner">
    <div style="font-size:7.5px;line-height:1.25">VANTO3 Pty Ltd<br>PO BOX 2047<br>Eastfield VIC 3095<br>admin@vanto3.com.au</div>
    <div style="margin-top:22px"><div class="brand-word">VANTO3</div><div class="brand-tag">PASSIVE FIRE PROTECTION</div></div>
    <div class="cert-title">FIRE/SMOKE SYSTEM<br>CERTIFICATE</div>
    <div class="label" style="margin-top:14px">CLIENT</div>
    <div class="big">Tall Oak Constructions Pty Ltd</div>
    <div class="label" style="margin-top:12px">JOB</div>
    <div class="big">The Arden Bayside<br>15 Arden Street, Bayside</div>
    <div class="cert-pill">CERTIFICATE NUMBER: 2264</div>
    <p><b>VANTO3 Pty. Ltd.</b> certifies that as part of our contracted works, we have carried out the above fire protection at <b>The Arden Bayside – 15 Arden Street, Bayside</b> as instructed <b>Ben Harlow of Tall Oak Constructions Pty Ltd</b></p>
    <p>These works have been completed and checked using the approved proprietary fire resistance tested products &amp; systems <b>as per AS1530 part 4 &amp; AS4072 part 1</b></p>
    <p>Any works that are modified, damaged or disturbed following completion are not covered by this certification.</p>
    <p>Installed in accordance with the manufacturer's specifications.</p>
    <div class="signed"><span>Signed <span class="sig" role="img" aria-label="Handwritten signature"></span></span><span>Name &nbsp;<b>Liam Carver</b></span><span>Date &nbsp;<b>16th January, 2026</b></span></div>
    <div style="color:var(--red);font-size:7.5px;margin-top:18px">VANTO3.COM.AU</div>
  </div>
</div>

</body>
</html>
```